Domestic violence resource cards for distribution to at-risk patients in an emergency department

Using the attached image(or very similar) and text document, a tri-fold business card is requested that integrates the image on the outside and the document content throughout the card's remaining faces. A creative format is requested, one that does not look like the typical cold, uncaring bullet point outlines that are found in similar resource projects. Bold or larger font sizes are requested for headings and body text is not required to be aligned or justified and the bullet points in the supplied document can be removed for creative license. Palattes should be clear, avoiding neons or implied target gender. Legibility is paramount, but again a creative presentation of a very serious subject is our goal. These cards are intended to be distributed to patients or others in the emergency department that may benefit from domestic violence resources. The business card size is mandatory so that the card can be concealed if needed by the receiver.
Updates

Reason: There are several revisions from designers that we are anxiously awaiting; we want to provide time for these designers to submit new designs but also continue spending time with their families and friends around the holiday season.

Target Market(s)

Patients and family in contact with emergency services

Industry/Entity Type

Healthcare

Contact Information for Business Card

Double sided tri-fold card with image on outer sides, text content and resource phone numbers on the exterior. When complete, the card should fold to standard US business card size.

Font styles to use
Other font styles liked:
• Designer's choice, but clear and legible

Requirements
Must have
• See above description. Card must be tri-fold, fold down to standard business card size, remain easily readable, and fold along the long edge.
Should not have
• Cartoon images; bloated fonts or clipart; bright, flashy neon or rainbow-like colors; additional graphics or charts.

```html
<!DOCTYPE html>
<html lang="en">
<head>
<meta charset="utf-8">
<title>Domestic Violence Resource Card</title>
<link href="https://fonts.googleapis.com/css2?family=Carlito:wght@400;700&family=Nunito+Sans:wght@600;700;800&family=Oswald:wght@600&display=swap" rel="stylesheet">
<style>
:root{
  --page:#ffffff;
  --frame:#b7bcc6;
  --frame-dark:#a4aab5;
  --paper:#f3f4f6;
  --paper-edge:#dfe2e7;
  --ink:#222428;
  --ink-soft:#3a3d42;
  --photo-dark:#1b2232;
  --photo-mid:#4d586c;
  --photo-light:#c9ced8;
  --title-grey:#a9acb1;
  --fold:#666a70;
}
*{box-sizing:border-box;margin:0;padding:0}
html,body{width:1200px;height:1048px;overflow:hidden;background:var(--page)}
.canvas{position:relative;width:1200px;height:1048px}
.panel{position:absolute;background:linear-gradient(180deg,var(--frame),var(--frame-dark))}
.panel--outer{left:62px;top:57px;width:528px;height:933px}
.panel--inner{left:620px;top:57px;width:530px;height:935px}
.paper{position:absolute;background:radial-gradient(ellipse at center,var(--page) 40%,var(--paper) 75%,var(--paper-edge) 100%);border-radius:14px}
.fold{position:absolute;left:590px;width:575px;border-top:1.5px dotted var(--fold)}
/* outer face */
.contacts{position:absolute;left:62px;width:528px;text-align:center;font-family:"Nunito Sans",sans-serif;color:var(--ink)}
.contacts--front{top:110px}
.contact-name{font-size:15px;font-weight:700;line-height:20px}
.contact-phone{font-size:15.5px;font-weight:800;letter-spacing:.5px;line-height:20px;margin-top:8px;margin-bottom:15px}
.contacts--back{top:676px;height:314px;transform:rotate(180deg);padding-top:40px}
.contacts--back .contact-phone{margin-top:6px;margin-bottom:12px}
.contact-text{font-size:15px;font-weight:800;letter-spacing:.5px;line-height:20px}
.contact-web{font-size:17px;font-weight:700;margin-top:26px}
.cover{position:absolute;left:62px;top:370px;width:528px;height:306px;background:linear-gradient(90deg,var(--photo-dark) 0%,var(--photo-mid) 35%,var(--photo-light) 55%,var(--photo-mid) 80%,var(--photo-dark) 100%)}
.cover-shade{position:absolute;left:0;right:0;bottom:0;height:80px;background:linear-gradient(180deg,transparent,var(--photo-dark))}
.cover-title{position:absolute;left:62px;top:28px;font-family:"Oswald",sans-serif;font-weight:600;font-size:40px;line-height:56px;letter-spacing:3px;color:var(--title-grey)}
.cover-web{position:absolute;left:0;width:100%;bottom:16px;padding-left:150px;font-family:"Nunito Sans",sans-serif;font-weight:700;font-size:17px;color:var(--page)}
/* inner face */
.section{position:absolute;font-family:"Carlito",sans-serif;color:var(--ink-soft)}
.section h2{font-weight:700;color:var(--ink);text-align:center}
.list{list-style:none}
.list li{position:relative;padding-left:14px}
.list li::before{content:"·";position:absolute;left:2px}
.section--questions{top:108px;left:650px;width:470px}
.section--questions h2{font-size:15.5px;line-height:22px}
.section--questions .list li{font-size:15.5px;line-height:19.8px}
.warning{font-weight:700;font-size:15.5px;line-height:20px;color:var(--ink);text-align:right;margin-top:3px;padding-right:2px}
.section--remember{top:380px;left:658px;width:460px}
.section--remember h2{font-size:13.5px;line-height:17px}
.section--remember .list li{font-size:13.5px;line-height:16.5px}
.section--remember .plan-heading{margin-top:6px;line-height:17px}
.section--remember .list.tips{margin-top:10px}
.section--remember .list.tips li{font-size:13.5px;line-height:17.8px}
.section--plan{top:688px;left:658px;width:462px}
.section--plan .list li{font-size:13.5px;line-height:17.8px}
</style>
</head>
<body>
<div class="canvas">
  <div class="panel panel--outer"></div>
  <div class="panel panel--inner"></div>

  <div class="paper" style="left:80px;top:74px;width:494px;height:300px"></div>
  <div class="paper" style="left:80px;top:672px;width:494px;height:300px"></div>
  <div class="paper" style="left:638px;top:74px;width:494px;height:294px"></div>
  <div class="paper" style="left:638px;top:374px;width:494px;height:300px"></div>
  <div class="paper" style="left:638px;top:678px;width:494px;height:296px"></div>

  <div class="fold" style="top:370px"></div>
  <div class="fold" style="top:676px"></div>

  <div class="contacts contacts--front">
    <div class="contact-name">National Family Safety Line</div>
    <div class="contact-phone">1-800-555-0142</div>
    <div class="contact-name">Harbor House Metro: Domestic Violence Crisis Resource</div>
    <div class="contact-phone">303-555-0187</div>
    <div class="contact-name">Crossway Domestic Violence Resources</div>
    <div class="contact-phone">303-555-0119</div>
    <div class="contact-name">The Open Door Center</div>
    <div class="contact-phone">1-888-555-0163</div>
  </div>

  <div class="cover" role="img" aria-label="Black and white photograph of a distressed woman sitting on the floor hugging her knees against a wall">
    <div class="cover-shade"></div>
    <div class="cover-title">NATIONAL<br>DOMESTIC<br>VIOLENCE</div>
    <div class="cover-web">www.safeharbornetwork.org</div>
  </div>

  <div class="contacts contacts--back">
    <div class="contact-name">Oak Branch Violence Resources</div>
    <div class="contact-phone">303-555-0176</div>
    <div class="contact-name">Quiet Bench: Sexual Assault Victim's Advocate</div>
    <div class="contact-phone">303-555-0134</div>
    <div class="contact-name">Care Is Respect: Teen Dating Resource</div>
    <div class="contact-text" style="margin-top:6px">1-866-555-0158</div>
    <div class="contact-text">or text “careis” to 55510</div>
    <div class="contact-web">www.safeharbornetwork.org</div>
  </div>

  <div class="section section--questions">
    <h2>DOES YOUR PARTNER EVER...</h2>
    <ul class="list">
      <li>Hit, kick, push, choke or slap you?</li>
      <li>Intimidate you with weapons or harmful objects?</li>
      <li>Force you to engage in sexual acts?</li>
      <li>Threaten to hurt you, your children or your friends/family?</li>
      <li>Threaten to deport you or tell others your personal information?</li>
      <li>Control where you go, who you talk to or who you make friends with?</li>
      <li>Keep, hide or destroy your most important things?</li>
      <li>Blame, embarrass, or criticize you, make you feel worthless or guilty?</li>
      <li>Control your food, money, medicines or medical care?</li>
    </ul>
    <p class="warning">You may be a victim of abuse or neglect!</p>
  </div>

  <div class="section section--remember">
    <h2>ALWAYS REMEMBER...</h2>
    <ul class="list">
      <li>You have a right to be safe anywhere</li>
      <li>You don't deserve to be hit or threatened</li>
      <li>Your children deserve to grow up without violence</li>
      <li>You have a right to protect you or your children until you are out of danger</li>
      <li>You are not alone</li>
      <li>You have choices</li>
    </ul>
    <h2 class="plan-heading">Leaving can be tough and very dangerous.<br>HERE ARE SOME TIPS TO HELP YOU PLAN FOR SAFETY:</h2>
    <ul class="list tips">
      <li>Know people you can talk to and ask them to call the police if they hear a disturbance coming from your home</li>
      <li>Teach your children how to contact the police or fire department</li>
      <li>Practice how to get you and your children out of your home quickly and safely</li>
      <li>Plan where you will go if you have to leave right away and know the location of local emergency shelters</li>
    </ul>
  </div>

  <div class="section section--plan">
    <ul class="list">
      <li>Leave copies of important papers, keys, cash, IDs, and medicine with a friend or relative you trust</li>
      <li>Have a small bag packed and ready at a friend or relative's house so you can leave quick</li>
      <li>Stay off social media or cancel you accounts so that you can't be found online or through your friends</li>
      <li>Do not talk about your plans in public areas or in mixed groups</li>
      <li>Open a credit card or bank account in your name only and do not use it until you are ready</li>
      <li>Keep a charged prepaid cell phone and a shelter hotline number ready for emergencies</li>
      <li>Review your plan often and only share with trusted friends or family</li>
      <li>Be careful: you are at most risk during the first 72 hours after leaving an abusive situation</li>
      <li>Seek help at a police station, firehouse or hospital if needed</li>
    </ul>
  </div>
</div>
</body>
</html>
```